YARD CRAFTERS "N" CO

catyering to driveway/patio floor construction and remodeling. Concrete, concrete pavers, asphalt, Landscaping, irrigation, pergolas and pools.

Target Market(s)

the home owner that wants to enhance their home

Industry/Entity Type

construction

Contact Information for Business Card

presidet: lino barrega email: yardcraftersnco@mailbox.test office/cell: 555 204 8813

Font styles to use
Sans Serif

Requirements
Must have
• logo should pop out
Nice to have
• the logo should demonstrate that we do exteriors only

```html
<!DOCTYPE html>
<html lang="en">
<head>
<meta charset="utf-8">
<title>Lino Barrega — Business Card</title>
<link rel="stylesheet" href="https://fonts.googleapis.com/css2?family=Open+Sans:wght@400;600;700;800&display=swap">
<style>
  :root {
    --backdrop: #232323;
    --card: #1f1f23;
    --card-edge: #e3202a;
    --red: #ec1c24;
    --grey: #9b9ca1;
    --white: #f2f2f2;
    --faint: #2c2c31;
    --faint-text: #34343a;
  }
  * { box-sizing: border-box; margin: 0; padding: 0; }
  html, body {
    width: 1200px; height: 780px; overflow: hidden;
    background: var(--backdrop);
    font-family: "Open Sans", Arial, sans-serif;
  }
  .canvas {
    position: relative; width: 1200px; height: 780px;
    display: flex; align-items: center; justify-content: center; gap: 40px;
  }
  .card {
    position: relative; width: 540px; height: 309px;
    background: var(--card);
    border-bottom: 4px solid var(--card-edge);
    box-shadow: 0 18px 40px rgba(0,0,0,.55);
    overflow: hidden;
  }

  /* Front */
  .card--front { display: flex; align-items: center; justify-content: center; }
  .brand { display: flex; align-items: center; gap: 12px; }
  .brand__mark { width: 18px; height: 18px; background: var(--red); }
  .brand__name { font-weight: 800; color: var(--grey); letter-spacing: .5px; }
  .card--front .brand__name { font-size: 46px; }

  /* Back */
  .card--back .brand { position: absolute; left: 34px; top: 70px; gap: 8px; }
  .card--back .brand__mark { width: 10px; height: 10px; }
  .card--back .brand__name { font-size: 24px; }

  .contact { position: absolute; right: 36px; top: 26px; text-align: right; }
  .contact__bar { position: absolute; right: -36px; top: 6px; width: 12px; height: 40px; background: var(--red); }
  .contact__name { font-size: 26px; font-weight: 700; line-height: 1.1; }
  .contact__first { color: var(--red); }
  .contact__last { color: var(--grey); }
  .contact__title { font-size: 13px; font-weight: 600; color: var(--white); margin-top: 2px; }
  .contact__lines { margin-top: 14px; font-size: 12.5px; color: var(--white); list-style: none; }
  .contact__lines li { display: flex; justify-content: flex-end; align-items: center; gap: 8px; margin-top: 4px; }
  .contact__lines svg { width: 12px; height: 12px; fill: none; stroke: var(--red); stroke-width: 2; }

  .services { position: absolute; left: 34px; bottom: 22px; list-style: none; font-size: 12.5px; color: var(--white); line-height: 1.45; }
  .services li { display: flex; align-items: center; gap: 9px; }
  .services li::before { content: ""; width: 8px; height: 8px; border-radius: 50%; background: var(--red); flex: none; }

  .watermark-brand { position: absolute; right: 20px; bottom: 28px; display: flex; align-items: center; gap: 10px; }
  .watermark-brand .brand__mark { width: 40px; height: 40px; background: var(--faint); }
  .watermark-brand .brand__name { font-size: 26px; color: var(--faint-text); }
</style>
</head>
<body>
<main class="canvas">
  <section class="card card--front" aria-label="Card front">
    <div class="brand">
      <span class="brand__mark"></span>
      <span class="brand__name">Lino Barrega</span>
    </div>
  </section>

  <section class="card card--back" aria-label="Card back">
    <div class="brand">
      <span class="brand__mark"></span>
      <span class="brand__name">Lino Barrega</span>
    </div>

    <div class="contact">
      <span class="contact__bar"></span>
      <p class="contact__name"><span class="contact__first">Lino</span> <span class="contact__last">Barrega</span></p>
      <p class="contact__title">Presidet</p>
      <ul class="contact__lines">
        <li>555 204 8813
          <svg viewBox="0 0 12 12" aria-hidden="true"><path d="M2 1.5 L4.5 1.5 L5.5 4 L4 5 Q5 7.5 7 8 L8 6.5 L10.5 7.5 L10.5 10 Q5 10.5 1.5 4.5 Z"/></svg>
        </li>
        <li>yardcraftersnco@mailbox.test
          <svg viewBox="0 0 12 12" aria-hidden="true"><rect x="1" y="2.5" width="10" height="7"/><path d="M1 2.5 L6 7 L11 2.5"/></svg>
        </li>
      </ul>
    </div>

    <ul class="services">
      <li>Concrete</li>
      <li>Asphalt</li>
      <li>Irrigation</li>
      <li>Landscaping</li>
      <li>Concrete pavers</li>
      <li>Pergolas and pools</li>
      <li>Catyering to driveway</li>
      <li>Patio floor construction and remodeling</li>
    </ul>

    <div class="watermark-brand" aria-hidden="true">
      <span class="brand__mark"></span>
      <span class="brand__name">Lino Barrega</span>
    </div>
  </section>
</main>
</body>
</html>
```